Harbour Wing Flights business card

I need a business card designed based on our logo -- designed by Studio Flock designers.

The logo is to be taken from our web site at www.harbourwingflights.com.au

I need to have this card designed quickly as its needed for business meetings
Updates

Hi Designers, Please see my updated brief for my business card. I have attached logo images and a brochure for inspiration... Regards, Gavin Trelford Harbour Wing Flights

Target Market(s)

Hotel owners and operators (concierge) and tourists to Australia

Industry/Entity Type

Business

Font styles to use
Sans Serif

Colors
84abd2
3176b5
85abd2
cedeec

Requirements
Must have
• Utilise our logo. Found on our web page www.harbourwingflights.com.au

SIDE 1
Must have my name: Gavin Trelford
Title:Owner
Phone number: 1300 418 396
Mobile:0461273958

SIDE 2
LOGO
PREPARE TO BE AMAZED! (see attached brochure for information and font style)
Nice to have
• Something that reflects aviation and tour with a light aircraft

```html
<!DOCTYPE html>
<html lang="en">
<head>
<meta charset="utf-8">
<title>Harbour Wing Flights – Business Card</title>
<link rel="stylesheet" href="https://fonts.googleapis.com/css2?family=Open+Sans:wght@400;600;700&display=swap">
<style>
  :root {
    --backdrop: #c4c8cf;
    --card-light: #ffffff;
    --card-shade: #cedeec;
    --brand-blue: #3176b5;
    --sky-blue: #84abd2;
    --charcoal: #454545;
    --ink: #3a3a3a;
    --white: #ffffff;
  }
  * { box-sizing: border-box; margin: 0; padding: 0; }
  html, body {
    width: 1200px; height: 866px; overflow: hidden;
    background: var(--backdrop);
    font-family: "Open Sans", Arial, sans-serif;
  }
  .stage {
    width: 1200px; height: 866px;
    display: flex; align-items: center; justify-content: center; gap: 40px;
  }
  .card {
    position: relative; width: 540px; height: 320px; overflow: hidden;
    background: radial-gradient(ellipse at 40% 45%, var(--card-light) 0%, var(--card-shade) 130%);
    box-shadow: 0 6px 18px rgba(0,0,0,0.18);
  }
  .brand {
    display: flex; align-items: center; gap: 10px;
    color: var(--charcoal); font-weight: 600; letter-spacing: 0.5px;
  }
  .brand-dot {
    width: 16px; height: 16px; border-radius: 50%; background: var(--brand-blue);
  }
  .back-lockup {
    position: absolute; left: 50%; top: 50%; transform: translate(-50%, -50%);
    display: flex; flex-direction: column; align-items: center; gap: 14px;
  }
  .back-lockup .brand { font-size: 22px; }
  .tagline {
    color: var(--brand-blue); font-weight: 700; font-size: 13px; letter-spacing: 2.5px;
  }
  .card-front .brand { position: absolute; left: 60px; top: 70px; font-size: 17px; }
  .card-art { position: absolute; inset: 0; }
  .holder { position: absolute; left: 26px; top: 168px; }
  .holder-name { color: var(--brand-blue); font-weight: 700; font-size: 19px; }
  .holder-title { color: var(--ink); font-size: 17px; margin-top: 2px; }
  .contact {
    position: absolute; right: 22px; top: 128px; text-align: right;
    color: var(--white); font-size: 12px; line-height: 18px; list-style: none;
  }
  .contact li { display: flex; justify-content: flex-end; align-items: center; gap: 5px; }
  .contact svg { width: 11px; height: 11px; fill: var(--white); }
</style>
</head>
<body>
<main class="stage">
  <section class="card card-back">
    <div class="back-lockup">
      <div class="brand"><span class="brand-dot"></span>Harbour Wing Flights</div>
      <p class="tagline">PREPARE TO BE AMAZED!</p>
    </div>
  </section>

  <section class="card card-front">
    <svg class="card-art" viewBox="0 0 540 320" aria-hidden="true">
      <path fill="var(--charcoal)" d="M372 0 H540 V320 H70 C210 312 300 262 330 160 C345 100 350 40 372 0 Z"/>
      <path fill="var(--brand-blue)" d="M354 0 C332 40 326 100 311 158 C283 256 190 298 0 300 V284 C176 282 268 250 296 158 C312 100 318 40 338 0 Z"/>
      <path fill="var(--sky-blue)" d="M188 270 C278 262 318 222 337 150 C330 228 288 272 188 270 Z"/>
    </svg>

    <div class="brand"><span class="brand-dot"></span>Harbour Wing Flights</div>

    <div class="holder">
      <p class="holder-name">Gavin Trelford</p>
      <p class="holder-title">Owner</p>
    </div>

    <ul class="contact">
      <li>12 Quayside Arcade</li>
      <li>Ferry Lane NSW</li>
      <li>1300 418 396
        <svg viewBox="0 0 24 24"><path d="M6.6 10.8a15 15 0 0 0 6.6 6.6l2.2-2.2a1 1 0 0 1 1-.25 11.4 11.4 0 0 0 3.6.6 1 1 0 0 1 1 1V20a1 1 0 0 1-1 1A17 17 0 0 1 3 4a1 1 0 0 1 1-1h3.5a1 1 0 0 1 1 1c0 1.25.2 2.45.6 3.6a1 1 0 0 1-.25 1z"/></svg>
      </li>
      <li>0461273958
        <svg viewBox="0 0 24 24"><path d="M7 1h10a2 2 0 0 1 2 2v18a2 2 0 0 1-2 2H7a2 2 0 0 1-2-2V3a2 2 0 0 1 2-2z M7 4v14h10V4z"/></svg>
      </li>
      <li>02 8104 5527
        <svg viewBox="0 0 24 24"><path d="M6 2h9l3 3v5H6z M3 11h18v10H3z M7 14h3v2H7z M12 14h3v2h-3z M7 17h3v2H7z M12 17h3v2h-3z"/></svg>
      </li>
      <li>hello@hwflights.com.au
        <svg viewBox="0 0 24 24"><path d="M2 5h20v14H2z M3 6l9 7 9-7" stroke="#454545" stroke-width="1.5"/></svg>
      </li>
      <li>www.harbourwingflights.com.au</li>
    </ul>
  </section>
</main>
</body>
</html>
```